Ardenwell Building and Property Services needs a business card design

We need a business card design for our building and property services business. We already have a logo we just need a creative design and layout on a business card. Emphasis on clean, modern, professional.
Our client targets are mainly body corporates, building managers, construction managers.
We are a building services company that lean more to structural repair of buildings, through concrete rectification and carbon fibre strengthening.
We also refurbish facades, rendering, painting etc
We target higher end body corporates in prestigious locations, hence why we'd like our cards to reflect professionalism, strength, efficiency

Target Market(s)

body corporates, building managers, construction managers

Industry/Entity Type

Construction

Contact Information for Business Card

Ardenwell is the main word, with 'Building and Property Services' underneath.
Level 17, 82 Harlow Street
MERRIDALE
Melbourne
Vic 3094
T: 9518 2736
Duncan Ferris - Director
dunardenwell@mailbox-example.com

Requirements
Must have
• Stand out on the back of the card- strong/ bold, company logo
• All of the contact details written above
Should not have
• I'd like the card to stand out, especially on the back. Id like the company logo to be prominent, although feel free to be creative around it. But remain clean and professional

```html
<!DOCTYPE html>
<html lang="en">
<head>
<meta charset="utf-8">
<title>Ardenwell Building and Property Services — Business Card</title>
<link href="https://fonts.googleapis.com/css2?family=Cinzel:wght@400;500&family=PT+Sans:wght@400&display=swap" rel="stylesheet">
<style>
  :root {
    --backdrop: #4a3537;
    --card: #231f20;
    --brand-blue: #1e9ad6;
    --text-light: #f2f2f2;
    --text-muted: #9a9a9a;
  }
  * { margin: 0; padding: 0; box-sizing: border-box; }
  html, body {
    width: 1200px; height: 1200px; overflow: hidden;
    background: var(--backdrop);
  }
  .canvas { position: relative; width: 1200px; height: 1200px; }
  .card {
    position: absolute; left: 218px; width: 766px; height: 437px;
    background: var(--card); border-radius: 18px;
  }
  .card--front { top: 114px; }
  .card--back { top: 652px; }

  .brand-mark {
    position: absolute; display: flex; flex-direction: column; align-items: center;
  }
  .brand-mark__square {
    width: 34px; height: 34px; background: var(--brand-blue); margin-bottom: 22px;
  }
  .brand-mark__name {
    font-family: "Cinzel", serif; font-weight: 400; color: var(--brand-blue);
    letter-spacing: 3px; line-height: 1;
  }
  .card--front .brand-mark { left: 0; right: 0; top: 150px; }
  .card--front .brand-mark__name { font-size: 58px; }

  .card--back .brand-mark { left: 60px; width: 272px; top: 138px; }
  .card--back .brand-mark__square { width: 30px; height: 30px; margin-bottom: 40px; }
  .card--back .brand-mark__name { font-size: 41px; letter-spacing: 2px; }
  .brand-mark__tagline {
    font-family: "Cinzel", serif; font-size: 10px; color: var(--text-muted);
    letter-spacing: 1.6px; text-transform: uppercase; margin-top: 6px;
  }

  .divider {
    position: absolute; left: 360px; top: 88px; width: 2px; height: 276px;
    background: var(--brand-blue);
  }
  .contact {
    position: absolute; left: 394px; top: 120px;
    font-family: "PT Sans", sans-serif; color: var(--text-light);
  }
  .contact__name {
    font-family: "Cinzel", serif; font-weight: 400; color: var(--brand-blue);
    font-size: 32px; line-height: 1; letter-spacing: 1px;
  }
  .contact__role { font-size: 19px; margin-top: 4px; }
  .contact__lines { margin-top: 30px; }
  .contact__line { display: flex; align-items: center; font-size: 19px; height: 26px; }
  .contact__icon { width: 18px; height: 14px; margin-right: 12px; fill: var(--brand-blue); }
  .contact__address { margin-top: 24px; font-size: 19px; line-height: 26px; }
</style>
</head>
<body>
<main class="canvas">
  <section class="card card--front" aria-label="Card front">
    <div class="brand-mark">
      <div class="brand-mark__square"></div>
      <div class="brand-mark__name">ARDENWELL</div>
    </div>
  </section>

  <section class="card card--back" aria-label="Card back">
    <div class="brand-mark">
      <div class="brand-mark__square"></div>
      <div class="brand-mark__name">ARDENWELL</div>
      <div class="brand-mark__tagline">Building and Property Services</div>
    </div>
    <div class="divider"></div>
    <div class="contact">
      <div class="contact__name">Duncan Ferris</div>
      <div class="contact__role">Director</div>
      <div class="contact__lines">
        <div class="contact__line">
          <svg class="contact__icon" viewBox="0 0 18 14" aria-hidden="true">
            <path d="M1 4 Q9 -1 17 4 L15 6 L12 5 L12 3.5 Q9 2.5 6 3.5 L6 5 L3 6 Z"/>
            <path d="M4 7 L6 6 L12 6 L14 7 L15 13 L3 13 Z"/>
            <circle cx="9" cy="9.5" r="1.8" fill="#231f20"/>
          </svg>9518 2736
        </div>
        <div class="contact__line">
          <svg class="contact__icon" viewBox="0 0 18 14" aria-hidden="true">
            <path d="M1 2 H17 V13 H1 Z M2.5 3.5 L9 8.5 L15.5 3.5 V11.5 H2.5 Z" fill-rule="evenodd"/>
          </svg>dunardenwell@mailbox-example.com
        </div>
      </div>
      <div class="contact__address">
        Level 17, 82 Harlow Street<br>
        MERRIDALE, Melbourne Vic 3094
      </div>
    </div>
  </section>
</main>
</body>
</html>
```